Gold Harbor Concierge

I need a website developed for our travel concierge service. I'm looking to be able to collect information and have the information collected directed to a inbox. I would also like to me able to manage the updates to the website myself. I also would like a mobile version of the website to be included. Our services include assistance with Bachelor Parties, Bachelorette Parties and Medical Tourism. We provide custom packages that include Airport Transportation, Lodging, Bilingual guides and any other special needs identified by our clients.
Industry/Entity Type
Travel
Coding
Coded - Design and coding required
Number of Pages Required
4 page
Look and feel

```html
<!DOCTYPE html>
<html lang="en">
<head>
<meta charset="UTF-8">
<title>Gold Harbor Concierge</title>
<link href="https://fonts.googleapis.com/css2?family=Poppins:wght@400;500;600;700;800&display=swap" rel="stylesheet">
<style>
:root{
  --gold:#df8c1f;
  --white:#ffffff;
  --bg-dark:#111214;
  --bg-mid:#1c1d1f;
  --bg-foot:#131416;
  --text-soft:#d6d6d6;
}
*{margin:0;padding:0;box-sizing:border-box}
html,body{width:1200px;height:4528px;overflow:hidden}
body{font-family:'Poppins',sans-serif;color:var(--white);background:var(--bg-dark);position:relative}
.abs{position:absolute}
.accent{color:var(--gold)}
.btn{position:absolute;background:var(--gold);color:var(--white);font-weight:600;font-size:22px;display:flex;align-items:center;justify-content:center}
.photo{position:absolute}

/* hero */
.hero{position:absolute;left:0;top:0;width:1200px;height:794px;
  background:linear-gradient(180deg,#1a1c22 0%,#55606a 18%,#8a99a6 35%,#7e6e5e 60%,#3e3732 100%)}
.hero::after{content:"";position:absolute;inset:0;background:linear-gradient(180deg,rgba(0,0,0,.55) 0%,rgba(0,0,0,0) 25%,rgba(0,0,0,.15) 100%)}
.nav a{position:absolute;top:80px;font-size:20px;font-weight:500;color:var(--white);text-decoration:none;z-index:2}
.nav a.active{color:var(--gold)}
.brand{position:absolute;left:450px;top:70px;width:300px;text-align:center;z-index:2}
.brand-mark{width:60px;height:60px;border:2px solid var(--white);border-radius:50%;margin:0 auto 10px}
.brand-name{font-size:24px;font-weight:500;letter-spacing:1px;color:var(--white)}
.hero-title{position:absolute;left:0;width:1200px;top:365px;text-align:center;font-size:70px;font-weight:800;z-index:2;text-shadow:0 2px 8px rgba(0,0,0,.4)}
.hero-sub{position:absolute;left:0;width:1200px;top:456px;text-align:center;font-size:28px;font-weight:700;z-index:2;text-shadow:0 2px 6px rgba(0,0,0,.4)}

/* sections */
.band{position:absolute;left:0;width:1200px}
.mid{background:var(--bg-mid)}
.dark{background:var(--bg-dark)}
.h-split{position:absolute;left:615px;font-size:48px;font-weight:700;line-height:55px}
.para{position:absolute;left:615px;width:520px;font-size:16.5px;line-height:37px;color:var(--text-soft)}
.sec-title{position:absolute;left:0;width:1200px;text-align:center;font-size:48px;font-weight:700;line-height:55px}

.card{position:absolute;width:328px;height:362px;overflow:hidden}
.card .label{position:absolute;left:20px;bottom:16px;font-size:33px;font-weight:700;line-height:38px;text-shadow:0 2px 6px rgba(0,0,0,.5)}
.feature .label{position:absolute;left:20px;bottom:40px;font-size:34px;font-weight:700;text-shadow:0 2px 6px rgba(0,0,0,.5)}
.feature .sub{position:absolute;left:20px;bottom:16px;font-size:18px;font-weight:600}

/* footer */
.foot-h{position:absolute;top:4198px;font-size:27px;font-weight:600;color:var(--gold)}
.foot-p{position:absolute;font-size:14px;line-height:27px;color:var(--text-soft)}
.contact-line{position:absolute;left:828px;font-size:15px;color:var(--text-soft)}
.social{position:absolute;top:4432px;width:20px;height:20px;border-radius:50%;background:var(--white)}
.corner{position:absolute;right:10px;top:4505px;font-size:12px;color:#aaa}
</style>
</head>
<body>

<header class="hero" role="img" aria-label="Friends celebrating by the sea with tropical drinks"></header>
<nav class="nav">
  <a class="active" style="left:99px">Home</a>
  <a style="left:206px">About Us</a>
  <a style="left:344px">Services</a>
  <a style="left:765px">Destinations</a>
  <a style="left:941px">News</a>
  <a style="left:1042px">Contact</a>
</nav>
<div class="brand">
  <div class="brand-mark"></div>
  <div class="brand-name">Gold Harbor Concierge</div>
</div>
<h1 class="hero-title">Gold Harbor Concierge</h1>
<p class="hero-sub">We are a travel concierge service.</p>
<div class="btn" style="left:508px;top:511px;width:186px;height:55px;z-index:2">Read More</div>

<!-- welcome -->
<section class="band mid" style="top:794px;height:638px"></section>
<div class="photo" style="left:74px;top:866px;width:421px;height:411px;background:linear-gradient(135deg,#3a1f4a,#8a2f6e 45%,#1e1a2a)" role="img" aria-label="Friends partying under falling confetti"></div>
<div class="photo" style="left:253px;top:1079px;width:334px;height:276px;background:linear-gradient(160deg,#1a1d24,#4a4038 55%,#b69a82)" role="img" aria-label="Women toasting with wine at a night terrace party"></div>
<h2 class="h-split" style="top:870px">Welcome to<br><span class="accent">Gold Harbor Concierge</span></h2>
<p class="para" style="top:992px">Sed ut perspiciatis unde omnis iste natus error sit voluptatem accusantium doloremque laudantium, totam rem aperiam, eaque ipsa quae ab illo inventore veritatis et quasi architecto beatae vitae dicta sunt explicabo. Nemo enim ipsam voluptatem quia voluptas sit aspernatur aut odit aut fugit, sed quia consequuntur magni dolores.</p>
<div class="btn" style="left:615px;top:1284px;width:188px;height:58px">Read More</div>

<!-- services -->
<section class="band dark" style="top:1432px;height:568px"></section>
<h2 class="sec-title" style="top:1483px">Our <span class="accent">Services</span></h2>
<div class="card" style="left:74px;top:1571px;background:linear-gradient(160deg,#4a2a4e,#2a1c20 60%,#14110f)" role="img" aria-label="Men toasting at a bachelor party">
  <div class="label">Bachelor<br>Parties</div></div>
<div class="card" style="left:436px;top:1571px;background:linear-gradient(160deg,#7a6e66,#4b7890 55%,#2b4f66)" role="img" aria-label="Women with pool floats at a bachelorette party">
  <div class="label">Bachelorette<br>Parties</div></div>
<div class="card" style="left:798px;top:1571px;background:linear-gradient(160deg,#5a5f66,#8b8c8e 50%,#3e3a38)" role="img" aria-label="Doctor standing in front of a departing airplane">
  <div class="label">Medical<br>Tourism</div></div>

<!-- custom packages -->
<section class="band mid" style="top:2000px;height:641px"></section>
<div class="photo" style="left:74px;top:2070px;width:421px;height:411px;background:linear-gradient(135deg,#a8552e,#5a2a2a 50%,#2a1e22)" role="img" aria-label="Group of friends laughing together on a couch"></div>
<div class="photo" style="left:253px;top:2281px;width:334px;height:277px;background:linear-gradient(180deg,#7aa3c8,#3d7a9a 35%,#3c6a2a 60%,#2a4a1e)" role="img" aria-label="Two women posing by the ocean among greenery"></div>
<h2 class="h-split" style="top:2074px">Custom<br><span class="accent">Packages</span></h2>
<p class="para" style="top:2196px">Sed ut perspiciatis unde omnis iste natus error sit voluptatem accusantium doloremque laudantium, totam rem aperiam, eaque ipsa quae ab illo inventore veritatis et quasi architecto beatae vitae dicta sunt explicabo. Nemo enim ipsam voluptatem quia voluptas sit aspernatur aut odit aut fugit, sed quia consequuntur magni dolores.</p>
<div class="btn" style="left:615px;top:2490px;width:225px;height:54px">View Packages</div>

<!-- destinations -->
<section class="band dark" style="top:2641px;height:645px"></section>
<h2 class="sec-title" style="top:2690px">Select a Destination to <span class="accent">Create</span><br><span class="accent">Your Party Package Now</span></h2>
<div class="card" style="left:74px;top:2848px;background:linear-gradient(160deg,#3a4a8a,#2a1c2a 55%,#120e12)" role="img" aria-label="Women celebrating at a nightclub">
  <div class="label">Dominican<br>Republic</div></div>
<div class="card" style="left:436px;top:2848px;background:linear-gradient(160deg,#8a2a1e,#4a1a18 55%,#1e0e0c)" role="img" aria-label="Crowd dancing at a party">
  <div class="label">Mexico</div></div>
<div class="card" style="left:798px;top:2848px;background:linear-gradient(160deg,#2a3038,#3a3e44 55%,#1a1c20)" role="img" aria-label="Friends in party hats celebrating">
  <div class="label">Colombia</div></div>

<!-- features -->
<section class="band mid" style="top:3286px;height:864px"></section>
<div class="card feature" style="left:74px;top:3351px;width:513px;height:344px;background:linear-gradient(160deg,#b8b2aa,#7a746e 55%,#4a4642)" role="img" aria-label="Friends relaxing in a rental room">
  <div class="label">Top Accommodations</div><div class="sub">Top Rated Party Rentals, All-Inclusive Resorts</div></div>
<div class="card feature" style="left:613px;top:3351px;width:513px;height:344px;background:linear-gradient(180deg,#3a3a3e,#9a7a52 45%,#c89a5a 60%,#3a3028)" role="img" aria-label="Friends jumping on a beach at sunset">
  <div class="label">Fun Destinations</div><div class="sub">Party with Your Buddies in Exotic DR &amp; Mexico</div></div>
<div class="card feature" style="left:74px;top:3727px;width:1052px;height:344px;background:linear-gradient(160deg,#b8bcc0,#7a7e72 45%,#3e4036)" role="img" aria-label="Hikers exploring outdoors">
  <div class="label">Thrilling Activites</div><div class="sub">Enjoy Exciting Nightlife &amp; Day Tours</div></div>

<!-- footer -->
<footer class="band" style="top:4150px;height:378px;background:var(--bg-foot)"></footer>
<div class="abs" style="left:74px;top:4210px;width:200px">
  <div style="width:56px;height:56px;border:2px solid var(--gold);border-radius:50%;margin-left:50px;margin-bottom:12px"></div>
  <div style="font-size:22px;font-weight:500;color:var(--gold);line-height:28px">Gold Harbor<br>Concierge</div>
</div>
<div class="foot-p" style="left:74px;top:4372px;font-size:12px;line-height:23px">Copyright © 2021. Company Name.<br>All Right Reserved</div>
<div class="social" style="left:74px"></div>
<div class="social" style="left:106px"></div>
<div class="social" style="left:138px"></div>
<div class="social" style="left:170px"></div>
<div class="social" style="left:228px"></div>

<div class="foot-h" style="left:360px">Email Subscribe</div>
<div class="foot-p" style="left:360px;top:4242px;width:340px">Sed ut perspiciatis unde omnis iste natus error sit voluptatem accusantium.</div>
<div class="abs" style="left:360px;top:4313px;width:334px;height:57px;background:var(--white);color:#333;font-size:14px;padding:18px 14px">Email Address</div>
<div class="btn" style="left:360px;top:4382px;width:334px;height:55px">Subscribe</div>

<div class="foot-h" style="left:794px">Contact Us</div>
<div class="foot-p" style="left:794px;top:4242px;width:340px">Sed ut perspiciatis unde omnis iste natus error sit voluptatem accusantium.</div>
<svg class="abs" style="left:796px;top:4318px" width="16" height="14" viewBox="0 0 16 14"><path d="M1 3 L5 1 L11 3 L15 1 V11 L11 13 L5 11 L1 13 Z" fill="var(--gold)"/></svg>
<div class="contact-line" style="top:4312px;line-height:27px">2280 Harborview Rd<br># 118, Savannah,<br>GA 31401</div>
<svg class="abs" style="left:796px;top:4408px" width="16" height="16" viewBox="0 0 16 16"><path d="M3 1 L6 1 L7 5 L5 6 Q6 9 10 11 L11 9 L15 10 V13 Q14 15 12 15 Q2 13 1 3 Q1 1 3 1 Z" fill="var(--gold)"/></svg>
<div class="contact-line" style="top:4404px">1-800-555-0142</div>
<svg class="abs" style="left:796px;top:4442px" width="16" height="12" viewBox="0 0 16 12"><rect width="16" height="12" rx="1" fill="var(--gold)"/><path d="M1 1 L8 7 L15 1" stroke="#131416" stroke-width="1.5" fill="none"/></svg>
<div class="contact-line" style="top:4438px">info@goldharborconcierge.com</div>
<div class="corner">x10</div>

</body>
</html>
```